Non-Profit Organization Needs WordPress websiteTo Empower Women

Our client is a Non-profit organization that requires a responsively-designed WordPress website to help publish their online magazine. This website will also feature their magazine publication that they publish quarterly. The design will need to be mobile-friendly, so it looks great on all devices.

The main purpose of this site is the following, in order of importance:
1. Educate economically-challenged women to improve their lives with blog content and their online Magazine.
2. Create a Membership community for these women to help one another. THE MAIN CALL-TO-ACTION ON THE SITE IS TO MOTIVATE THE READERS TO JOIN THE FREE MEMBERSHIP COMMUNITY.
3. Recognize and Identify the contributing Organizations, and to motivate the organizations to donate money to the non-profit organization.

Here is information from the client about what they want for their website:
*********************************************************************************************
It needs to have two entrances to content: Organizations & Readers; Don't like cluttered which some magazine formats seem to be. Like edgy, yet feminine. Not sweet. Easy to navigate and find what one comes to find. Colorful.

We need: A Resources area, a Donation button prominently placed on the site, section for archived magazine articles; Place for translated issues. We will want to have a private Membership section on the site. (NOTE: These requests should be used to help create the site's navigation menu.)

Here are example websites the client likes and why. Please use them as inspiration.
http:://www.brindleloft.example color, simple design w cool buttons, uncluttered
http:://www.corvetide.example emotion with the color, ease of getting around
http:://www.quellmarrow7.example the second page has the color sections that take you to next page
http:://www.tamsinreedjournal.example not sweetly feminine, perhaps community style
http:://www.velkarun.example use of clear symbols, newer design/graphics look

Target Market(s)

The website targets 2 different audiences: Organizations that help to provide services and help to the website readers, and the Readers themselves. The Readers are mostly economically-challenged females that need inspiration and help. The Readers should be considered the Primary Target Audience, with the Organizations being secondary.

Industry/Entity Type

Non-Profit

Font styles to use
Sans Serif

Colors
f37022
fece3e

Requirements
Must have
• The final design MUST, MUST, MUST be created using Separate PSD layers for each element and graphic! PLEASE create a professional layer structure within your design, so we can code it properly.

Please do NOT use Graphics/Images where Text should be used. Examples of this are the business address, phone number, etc.

The website home page design should identify its two main audiences, the Organizations and the Readers. The main call to action is to invite the Readers to become free members of their membership community.

There MUST be an area on the home page where their online magazine can be embedded onto their site OR an image button etc that leads to the magazine. They use the http://plimbrook.example/ system to create the magazine and then embed the issues on their site. Alternatively, you could create a button, image, area, etc, where the user can click the image and then go to the magazine.

A membership login field OR a button that leads to a Members login area.

A small area on the website that either Brovanta or advertising can be used, and this MUST be BELOW the FOLD.

The site must project a sense of hope and/or empowerment for its Readers. The imagery should resonate with females who want to be inspired.
Nice to have
• There should be links or buttons to identify Spanish-speaking Readers and Portuguese-speaking Readers.
Should not have
• NO Gallery Sliders or Photo Sliders

```html
<!DOCTYPE html>
<html lang="en">
<head>
<meta charset="utf-8">
<title>RiseWell Magazine</title>
<link rel="stylesheet" href="https://fonts.googleapis.com/css2?family=Questrial&display=swap">
<style>
:root{
  --orange:#f37022;
  --orange-dark:#d85c12;
  --orange-deep:#c74f0e;
  --yellow:#fece3e;
  --ink:#2b2b2b;
  --band:#f4f4f4;
  --white:#ffffff;
}
*{box-sizing:border-box;margin:0;padding:0}
html,body{width:764px;height:1200px;overflow:hidden;background:var(--white)}
body{font-family:"Questrial",sans-serif;color:var(--ink);position:relative}
.abs{position:absolute}
a{color:inherit;text-decoration:none}

/* top bar */
.topbar{left:0;top:0;width:764px;height:28px;background:var(--yellow)}
.account-links{left:110px;top:0;display:flex;height:28px}
.account-links a{color:var(--white);font-size:12px;letter-spacing:.5px;line-height:28px;width:93px;text-align:center;border-left:1px solid rgba(255,255,255,.45)}
.account-links a:last-child{border-right:1px solid rgba(255,255,255,.45)}
.social-dots{right:109px;top:4px;display:flex;gap:7px}
.social-dots span{width:20px;height:20px;border-radius:50%}
.social-dots span:nth-child(1){background:#3b5998}
.social-dots span:nth-child(2){background:#2aa3ef}
.social-dots span:nth-child(3){background:#d34836}
.social-dots span:nth-child(4){background:#3f729b}

/* header */
.brand{left:110px;top:52px;font-size:50px;color:var(--orange);letter-spacing:-1px;line-height:60px}
.tagline{left:434px;top:46px;width:221px;height:75px;background:var(--orange);border-radius:6px;color:var(--white);font-size:11.5px;line-height:14px;padding:9px 18px;white-space:nowrap}
.tagline::before{content:"";position:absolute;left:-8px;top:30px;border:8px solid transparent;border-left:0;border-right-color:var(--orange)}
.tagline b{font-weight:700}
.tagline .hi{color:#5a2200}
.tagline i{font-style:italic}

/* nav */
.nav{left:0;top:138px;width:764px;height:49px;background:var(--orange)}
.nav ul{position:absolute;left:110px;top:0;display:flex;list-style:none;height:49px}
.nav li{color:var(--white);font-size:14.5px;line-height:49px;text-align:center;white-space:nowrap;border-right:1px solid rgba(255,255,255,.2)}
.nav li.active{background:var(--orange-dark)}
.nav li:nth-child(1){width:68px}
.nav li:nth-child(2){width:75px}
.nav li:nth-child(3){width:105px}
.nav li:nth-child(4){width:101px}
.nav li:nth-child(5){width:86px;border-right:0}
.nav-donate{left:554px;top:11px;width:91px;height:28px;border-radius:14px;background:var(--white);color:var(--orange);font-size:14px;font-weight:700;text-align:center;line-height:28px;letter-spacing:.5px}

/* hero */
.hero-photo{left:0;top:187px;width:764px;height:273px;background:linear-gradient(90deg,#c9b8ab 0%,#e6d9cf 30%,#d9cec6 55%,#b9a69a 100%)}
.hero-copy{left:361px;top:248px;font-size:14.5px;line-height:26.5px;color:var(--ink);white-space:nowrap}
.hero-copy .mag{color:var(--orange);font-weight:700;font-style:italic}
.hero-copy .mag em{color:var(--ink)}
.btn{position:absolute;border-radius:19px;color:var(--white);text-align:center;font-size:16px;letter-spacing:.5px}
.hero-donate{left:361px;top:362px;width:140px;height:36px;line-height:36px;background:var(--yellow)}
.hero-member{left:508px;top:362px;width:141px;height:36px;line-height:36px;background:var(--orange)}

/* welcome */
.welcome{left:0;top:460px;width:764px;height:275px;background:var(--yellow)}
.welcome-title{left:0;top:485px;width:764px;text-align:center;font-size:16px;font-weight:400}
.welcome-title span{color:var(--orange);font-style:italic;font-weight:700}
.issue{width:86px;height:86px;border-radius:50%;border:3px solid var(--orange);overflow:hidden;top:537px}
.issue .cover{position:absolute;inset:0}
.issue .read{position:absolute;left:0;right:0;top:38px;height:14px;background:rgba(40,40,40,.75);color:var(--white);font-size:9px;text-align:center;line-height:14px}
.welcome-text{left:0;top:637px;width:764px;font-size:9.3px;line-height:14px;text-align:center;color:#3a2a10;white-space:nowrap}
.read-more{left:332px;top:689px;width:99px;height:29px;border-radius:15px;background:var(--white);font-size:10px;text-align:center;line-height:29px;letter-spacing:.5px}

/* blog & video */
.section-head{top:745px;font-size:26px;letter-spacing:.5px;font-weight:400}
.divider{left:388px;top:745px;width:1px;height:205px;background:#eeeeee}
.blog-photo{width:96px;height:96px;border-radius:50%;top:795px;border:3px solid #eeeeee}
.caption{font-size:9px;line-height:12.5px;top:909px;white-space:nowrap}
.video-frame{left:410px;top:794px;width:225px;height:108px;border-radius:4px;background:linear-gradient(90deg,#dcd6cc 0%,#e9e4dc 40%,#caa996 65%,#4b4b52 100%)}
.play{left:497px;top:823px}

/* membership band */
.join-band{left:0;top:958px;width:764px;height:50px;background:var(--band)}
.join-text{left:113px;top:972px;font-size:18px;white-space:nowrap}
.join-text b{color:var(--orange);font-weight:700}
.subscribe{left:493px;top:968px;width:143px;height:30px;line-height:30px;background:var(--orange-deep);font-size:15px;font-weight:700;border-radius:15px}

/* footer */
.footer{left:0;top:1008px;width:764px;height:158px;background:var(--orange)}
.foot-head{top:1035px;font-size:16px;letter-spacing:.5px;color:var(--white);font-weight:400}
.foot-small{font-size:9.5px;color:var(--white)}
.news-input{left:108px;top:1085px;width:112px;height:22px;background:var(--white);color:var(--orange);font-size:8px;line-height:22px;padding-left:6px}
.news-btn{left:108px;top:1112px;width:112px;height:24px;background:var(--orange-deep);border:1px solid rgba(255,255,255,.7);font-size:8px;font-weight:700;text-align:center;line-height:22px;color:var(--white)}
.mag-thumb{width:34px;height:34px;border-radius:50%;border:2px solid var(--white)}
.social-list{left:410px;top:1066px;list-style:none}
.social-list li{font-size:8.5px;height:20px;display:flex;align-items:center;gap:6px;color:var(--white)}
.social-list li i{width:12px;height:12px;border-radius:50%;background:var(--white);opacity:.85}
.quote{left:541px;top:1066px;width:110px;height:37px;border:1px solid var(--white);border-radius:8px;font-size:8px;line-height:10px;padding:3px 8px;color:var(--white)}
.quote::after{content:"";position:absolute;left:14px;bottom:-7px;border:6px solid transparent;border-bottom:0;border-top-color:var(--white)}
.avatar{left:545px;top:1110px;width:34px;height:34px;border-radius:50%;border:2px solid var(--white);background:linear-gradient(135deg,#f3d6a6,#c79f72)}
.author{left:584px;top:1120px;font-size:8.5px;line-height:10px;color:var(--white)}
.copyright{left:0;top:1176px;width:764px;text-align:center;font-size:8.5px;color:#9a9a9a}
</style>
</head>
<body>

<div class="abs topbar"></div>
<nav class="abs account-links"><a href="#">REGISTER</a><a href="#">LOGIN</a></nav>
<div class="abs social-dots" aria-label="Social links"><span></span><span></span><span></span><span></span></div>

<div class="abs brand">RiseWell</div>
<div class="abs tagline">The <b>MAGAZINE</b> For The<br><b class="hi">Empowerment</b> And<br><b class="hi">Enrichment</b> Of Today's<br><i>Inner City Women</i></div>

<div class="abs nav">
  <ul>
    <li class="active">Home</li><li>About</li><li>Participate</li><li>Resources</li><li>Contact</li>
  </ul>
  <a class="abs nav-donate" href="#">DONATE</a>
</div>

<div class="abs hero-photo" role="img" aria-label="Photo of a smiling woman in a knit hat and scarf looking upward in a soft autumn park"></div>
<p class="abs hero-copy"><span class="mag">RiseWell <em>Magazine</em></span> Is A Quarterly<br>Publication That Exists To Empower And<br>Enrich Today's Inner-city Woman. There<br>Are Several Ways You Can Participate...</p>
<a class="btn hero-donate" href="#">DONATE</a>
<a class="btn hero-member" href="#">MEMBERSHIP</a>

<section class="abs welcome"></section>
<h2 class="abs welcome-title">Welcome to <span>RiseWell</span></h2>
<div class="abs issue" style="left:135px"><div class="cover" role="img" aria-label="Magazine issue cover in red, green and yellow tones" style="background:linear-gradient(160deg,#d8e8c8 0%,#c0392b 55%,#e8a33a 100%)"></div><div class="read">READ</div></div>
<div class="abs issue" style="left:270px"><div class="cover" role="img" aria-label="Magazine issue cover with a red heart motif" style="background:linear-gradient(160deg,#f3f3f3 0%,#e24a4a 55%,#f3eee4 100%)"></div><div class="read">READ</div></div>
<div class="abs issue" style="left:406px"><div class="cover" role="img" aria-label="Magazine issue cover in blue and teal tones" style="background:linear-gradient(160deg,#cfe3f0 0%,#4d7c8e 55%,#2c3e3a 100%)"></div><div class="read">READ</div></div>
<div class="abs issue" style="left:543px"><div class="cover" role="img" aria-label="Magazine issue cover with a colourful flower" style="background:linear-gradient(160deg,#7b3c9c 0%,#e56a2e 55%,#f7d7a0 100%)"></div><div class="read">READ</div></div>
<p class="abs welcome-text">You're here because you care about people in the inner city. You don't see them as a problem or individuals to<br>ignore. No, like those of us on the RiseWell team, you see wonderful individuals each with a story to tell. You know<br>there is great potential to rise above difficult circumstances and you want to help them reach their goals.</p>
<a class="abs read-more" href="#">READ MORE</a>

<h2 class="abs section-head" style="left:110px">BLOG</h2>
<h2 class="abs section-head" style="left:408px">VIDEO</h2>
<div class="abs divider"></div>
<div class="abs blog-photo" style="left:116px;background:linear-gradient(160deg,#e8e2da,#b89a86)" role="img" aria-label="Blog photo of a laughing woman carrying shopping bags"></div>
<div class="abs blog-photo" style="left:262px;background:linear-gradient(160deg,#d9d4cc,#c8363a)" role="img" aria-label="Blog photo of a woman in a red jacket"></div>
<p class="abs caption" style="left:108px">"When's the next one?"<br>&nbsp;said one lady who gives out<br>extra issues to her neighbors.</p>
<p class="abs caption" style="left:254px">"Oh, you have Spanish! That is<br>really going to help in one of<br>our neighborhood areas."</p>
<div class="abs video-frame" role="img" aria-label="Video still of a woman beside a magazine cover"></div>
<svg class="abs play" width="50" height="50" viewBox="0 0 50 50" aria-hidden="true"><circle cx="25" cy="25" r="22" fill="#fff" stroke="#111" stroke-width="3"/><path d="M19 14 L36 25 L19 36 Z" fill="#111"/></svg>
<p class="abs caption" style="left:410px">"Where's this church? I want to go there!" This comment<br>was overheard at an outreach in a park where RiseWell<br>was being given away to the women.</p>

<div class="abs join-band"></div>
<p class="abs join-text">JOIN THE <b>FREE MEMBERSHIP COMMUNITY</b></p>
<a class="btn subscribe" href="#">SUBSCRIBE</a>

<footer class="abs footer"></footer>
<h3 class="abs foot-head" style="left:108px">NEWSLETTER</h3>
<h3 class="abs foot-head" style="left:264px">MAGAZINE</h3>
<h3 class="abs foot-head" style="left:411px">SOCIAL</h3>
<h3 class="abs foot-head" style="left:541px">TESTIMONIAL</h3>
<p class="abs foot-small" style="left:108px;top:1067px">subscribe the newsletter</p>
<div class="abs news-input">NEWSLETTER</div>
<div class="abs news-btn">SUBSCRIBE</div>
<div class="abs mag-thumb" style="left:262px;top:1070px;background:linear-gradient(160deg,#4d7c8e,#2c3e3a)" role="img" aria-label="Magazine issue thumbnail"></div>
<div class="abs mag-thumb" style="left:314px;top:1070px;background:linear-gradient(160deg,#7b3c9c,#e56a2e)" role="img" aria-label="Magazine issue thumbnail"></div>
<div class="abs mag-thumb" style="left:262px;top:1109px;background:linear-gradient(160deg,#c0392b,#e8a33a)" role="img" aria-label="Magazine issue thumbnail"></div>
<div class="abs mag-thumb" style="left:314px;top:1109px;background:linear-gradient(160deg,#f3f3f3,#e24a4a)" role="img" aria-label="Magazine issue thumbnail"></div>
<ul class="abs social-list">
  <li><i></i>KINLOOP</li><li><i></i>CHIRPWAVE</li><li><i></i>GATHERNET</li><li><i></i>SNAPFOLIO</li>
</ul>
<div class="abs quote">"Oh, you have Spanish! That is really going to help in one of</div>
<div class="abs avatar" role="img" aria-label="Portrait of the quoted community partner"></div>
<p class="abs author">Dana Morrow,<br>Harbor of Light</p>

<p class="abs copyright">Copyrights © 2014, RiseWell. All Right Reserved.</p>

</body>
</html>
```